New Mechanical Maintenance business needs website

New Mechanical Maintenance business in Perth Western Australia needs a nice and easy to navigate website. Showing what we do and how we can be the right fit for other small to medium size business by offering personalized service from our highly skilled team. We deal with both fixed plant repairs like food and chemical processing facilities to heavy equipment like drill rigs, Large boats and earthmoving equipment.

Target Market(s)

Small to medium business to offer personalized services/packages

Industry/Entity Type

e deal with both fixed plant repairs like food and chemical processing facilities to heavy equipment like drill rigs, Large boats and earthmoving equipment.

Coding

Coded - Design and coding required

Number of Pages Required

4 page

Font styles to use
Serif

Colors
0054AA
0677BA
7BADD7
CADEEF
E8F1F8

Requirements
Must have
• A website that is easy to navigate but covers off on the range of services/maintenance we can provide

```html
<!DOCTYPE html>
<html lang="en">
<head>
<meta charset="utf-8">
<title>Ostrevane Maintenance</title>
<link href="https://fonts.googleapis.com/css2?family=Raleway:wght@600;700&family=Roboto:wght@400;500;700&display=swap" rel="stylesheet">
<style>
:root{
  --blue:#0054AA;
  --blue-mid:#0677BA;
  --blue-soft:#7BADD7;
  --blue-pale:#CADEEF;
  --blue-bg:#E8F1F8;
  --slate:#4f5e7e;
  --bar:#5b6069;
  --text:#6b6f76;
  --dark:#222;
  --white:#fff;
  --star:#f5a623;
}
*{margin:0;padding:0;box-sizing:border-box}
html,body{width:1200px;height:3923px;overflow:hidden}
body{font-family:'Roboto',sans-serif;color:var(--text);background:var(--white);position:relative}
a{color:inherit;text-decoration:none}
.abs{position:absolute}
.btn{position:absolute;background:var(--blue);color:var(--white);font-weight:700;font-size:14px;display:flex;align-items:center;justify-content:center;gap:8px;text-transform:uppercase}
.btn svg{width:13px;height:13px}
.h-section{font-family:'Raleway',sans-serif;font-weight:700;font-size:36px;color:var(--slate);text-align:center;position:absolute;left:0;width:1200px}

/* top bar */
.topbar{top:0;left:0;width:1200px;height:37px;background:var(--bar);color:#eef;font-size:13px;z-index:3}
.topbar .item{position:absolute;top:11px;display:flex;align-items:center;gap:7px}
.topbar .item svg{width:11px;height:11px;fill:#fff}
.topbar .social{position:absolute;top:7px;right:144px;display:flex;gap:9px}
.topbar .social span{width:22px;height:22px;border-radius:50%;background:#454950}

/* nav */
.nav{top:37px;left:0;width:1200px;height:81px;background:var(--white);z-index:2}
.logo-badge{position:absolute;left:138px;top:-38px;width:160px;height:160px;border-radius:50%;background:var(--white)}
.logo{position:absolute;left:160px;top:24px;display:flex;align-items:center;gap:8px;font-weight:700;font-size:17px;color:var(--bar);letter-spacing:1px}
.logo .mark{width:30px;height:30px;border-radius:50%;background:var(--bar)}
.menu{position:absolute;left:461px;top:31px;display:flex;gap:29px;font-size:14px;color:var(--dark);font-weight:500}
.nav .btn{left:926px;top:21px;width:130px;height:40px}

/* hero */
.hero{top:118px;left:0;width:1200px;height:602px;background:linear-gradient(180deg,#3a4560 0%,#6a5a52 14%,#2b3954 32%,#3b4d6c 60%,#4a4c55 80%,#2f3a50 100%)}
.hero h1{position:absolute;top:196px;width:1200px;text-align:center;font-family:'Raleway',sans-serif;font-weight:700;font-size:45px;color:var(--white)}
.hero p{position:absolute;top:268px;left:360px;width:480px;text-align:center;color:var(--white);font-size:15.5px;font-weight:500;line-height:26px}
.hero .btn{left:514px;top:348px;width:170px;height:47px;font-size:15px}

/* about */
.about-img{left:144px;top:792px;width:456px;height:370px;background:linear-gradient(160deg,#1f3b5c,#4f7fa6 45%,#9a8a6a 70%,#2c4a6a)}
.about .eyebrow{left:659px;top:806px;font-family:'Raleway',sans-serif;font-weight:700;font-size:20px;color:var(--slate)}
.about h2{left:659px;top:834px;font-family:'Raleway',sans-serif;font-weight:700;font-size:32px;color:var(--slate)}
.about p{left:659px;width:397px;font-size:13.5px;line-height:24px;color:var(--text);text-align:justify}
.about .btn{left:659px;top:1100px;width:145px;height:43px;font-size:13.5px}
.call{left:834px;top:1100px;display:flex;align-items:center;gap:12px}
.call .ico{width:41px;height:41px;border-radius:50%;background:var(--blue);display:flex;align-items:center;justify-content:center}
.call .ico svg{width:20px;height:20px;fill:#fff}
.call small{display:block;font-size:11px;color:var(--text)}
.call strong{font-size:17px;color:var(--dark);letter-spacing:.5px}

/* services */
.services{top:1248px;left:0;width:1200px;height:1064px;background:var(--blue-bg)}
.card{position:absolute;width:287px;height:357px;background:var(--white);box-shadow:0 2px 8px rgba(0,0,0,.12);text-align:center}
.card .photo{height:180px}
.card .icon{position:absolute;left:112px;top:149px;width:62px;height:62px;border-radius:50%;background:var(--white);display:flex;align-items:center;justify-content:center}
.card .icon svg{width:34px;height:34px;stroke:var(--blue);fill:none;stroke-width:1.6}
.card h3{margin-top:50px;font-size:17.5px;font-weight:500;color:var(--dark)}
.card p{margin:12px auto 0;width:250px;font-size:13px;line-height:22px;color:#555}
.card .more{display:inline-flex;align-items:center;gap:6px;margin-top:14px;font-size:13px;font-weight:700;color:var(--blue);text-decoration:underline}
.card .more svg{width:12px;height:12px}

/* testimonial */
.testi{top:2312px;left:0;width:1200px;height:439px;background:linear-gradient(180deg,#56638f,#4a5888 60%,#5b6890)}
.testi h2{position:absolute;top:65px;width:1200px;text-align:center;font-family:'Raleway',sans-serif;font-weight:700;font-size:36px;color:var(--white)}
.quote{position:absolute;top:150px;width:381px;height:214px;background:var(--white);border-radius:40px}
.quote .q{position:absolute;left:92px;top:18px;font-family:'Raleway',sans-serif;font-size:72px;font-weight:700;color:var(--slate);line-height:72px}
.quote p{position:absolute;left:95px;top:78px;width:255px;font-size:13px;line-height:22px;color:#777}
.quote .name{position:absolute;left:95px;top:155px;font-size:15px;font-weight:500;color:var(--dark)}
.quote .stars{position:absolute;left:95px;top:176px;color:var(--star);font-size:15px;letter-spacing:1px}
.avatar{position:absolute;width:106px;height:106px;border-radius:50%;background:linear-gradient(160deg,#c7cdd6,#8796ab);border:3px solid var(--white);top:205px}
.arrow{position:absolute;top:242px}
.arrow svg{width:22px;height:34px;stroke:#e6e9f2;stroke-width:3;fill:none}

/* work */
.work-tile{position:absolute}
.zoom{position:absolute;left:50%;top:50%;width:44px;height:44px;margin:-22px 0 0 -22px;border-radius:50%;background:var(--white);display:flex;align-items:center;justify-content:center}
.zoom svg{width:18px;height:18px;stroke:var(--dark);stroke-width:2.4;fill:none}

/* footer */
.footer{top:3585px;left:0;width:1200px;height:338px;background:var(--bar);color:#e6e8ee}
.f-logo{position:absolute;left:160px;top:88px;display:flex;align-items:center;gap:10px;font-weight:700;font-size:17px;letter-spacing:1px;color:var(--white)}
.f-logo .mark{width:34px;height:34px;border-radius:50%;background:var(--white)}
.f-social{position:absolute;left:168px;top:190px;display:flex;gap:8px}
.f-social span{width:30px;height:30px;border-radius:50%;border:1.5px solid #cfd3da}
.f-col{position:absolute;top:56px}
.f-col h4{font-size:15px;font-weight:500;color:var(--white);margin-bottom:16px}
.f-col li{list-style:none;font-size:12.5px;line-height:24px;color:#d4d7dd}
.contact-row{display:flex;gap:12px;margin-bottom:10px}
.contact-row svg{width:12px;height:12px;fill:#fff;margin-top:3px;flex:none}
.contact-row b{display:block;font-size:11px;font-weight:700;color:var(--white)}
.contact-row span{font-size:12.5px;line-height:18px;color:#d4d7dd}
.f-line{position:absolute;left:144px;top:273px;width:912px;height:1px;background:#737883}
.copy{position:absolute;top:296px;left:418px;font-size:13px;color:#d4d7dd}
.to-top{position:absolute;left:1073px;top:252px;width:32px;height:32px;border-radius:50%;background:var(--blue);display:flex;align-items:center;justify-content:center}
.to-top svg{width:14px;height:14px;stroke:#fff;stroke-width:2.5;fill:none}
</style>
</head>
<body>

<header class="abs topbar">
  <div class="item" style="left:144px"><svg viewBox="0 0 16 12"><path d="M0 0h16v12H0z M0 0l8 6 8-6" /></svg>info@ostrevanemaint.com</div>
  <div class="item" style="left:362px"><svg viewBox="0 0 24 24"><path d="M6.6 10.8a15 15 0 006.6 6.6l2.2-2.2c.3-.3.7-.4 1-.2 1.1.4 2.3.6 3.6.6.6 0 1 .4 1 1V20c0 .6-.4 1-1 1A17 17 0 013 4c0-.6.4-1 1-1h3.5c.6 0 1 .4 1 1 0 1.3.2 2.5.6 3.6.1.3 0 .7-.2 1z"/></svg>+1 555 010 2040</div>
  <div class="item" style="left:515px"><svg viewBox="0 0 24 24"><circle cx="12" cy="12" r="10" fill="none" stroke="#fff" stroke-width="3"/><path d="M11 6h2v7h-2z"/></svg>Hours: 8am - 5pm : Mon - Fri</div>
  <div class="social"><span></span><span></span><span></span><span></span></div>
</header>

<nav class="abs nav">
  <div class="logo-badge"></div>
  <a class="logo" href="#"><span class="mark"></span>OSTREVANE</a>
  <div class="menu"><a href="#">Home</a><a href="#">Our Services</a><a href="#">About Us</a><a href="#">Our Work</a><a href="#">Contact Us</a></div>
  <a class="btn" href="#">Get a Quote</a>
</nav>

<section class="abs hero" role="img" aria-label="Industrial processing plant with storage tanks at dusk">
  <h1>OSTREVANE MAINTENANCE</h1>
  <p>Lorem ipsum dolor sit amet, consectetur adipiscing elit, sed do incididunt ut labore et dolore magna aliqua.</p>
  <a class="btn" href="#">Get Started <svg viewBox="0 0 16 16"><circle cx="8" cy="8" r="8" fill="#fff"/><path d="M6.5 4.5L10 8l-3.5 3.5" stroke="#0054AA" stroke-width="2" fill="none"/></svg></a>
</section>

<section class="about">
  <div class="abs about-img" role="img" aria-label="Engineers in hard hats walking between large pipelines"></div>
  <div class="abs eyebrow">WELCOME TO</div>
  <h2 class="abs">OSTREVANE MAINTENANCE</h2>
  <p class="abs" style="top:890px">Lorem ipsum dolor sit amet, consectetur adipiscing elit, sed do eiusmod tempor incididunt ut labore et dolore magna aliqua. Ut enim ad minim veniam, quis nostrud exercitation ullamco laboris nisi ut aliquip ex ea commodo consequat.</p>
  <p class="abs" style="top:998px">Duis aute irure dolor in reprehenderit in voluptate velit esse cillum dolore eu fugiat nulla pariatur. Excepteur sint occaecat cupidatat qui officia deserunt mollit anim id est laborum.</p>
  <a class="btn" href="#">More About Us</a>
  <div class="abs call">
    <div class="ico"><svg viewBox="0 0 24 24"><path d="M6.6 10.8a15 15 0 006.6 6.6l2.2-2.2c.3-.3.7-.4 1-.2 1.1.4 2.3.6 3.6.6.6 0 1 .4 1 1V20c0 .6-.4 1-1 1A17 17 0 013 4c0-.6.4-1 1-1h3.5c.6 0 1 .4 1 1 0 1.3.2 2.5.6 3.6.1.3 0 .7-.2 1z"/></svg></div>
    <div><small>Call Us Today</small><strong>(555) 010-2040</strong></div>
  </div>
</section>

<section class="abs services">
  <h2 class="h-section" style="top:52px">OUR SERVICES</h2>

  <article class="card" style="left:144px;top:125px">
    <div class="photo" role="img" aria-label="Refinery pipework lit at night" style="background:linear-gradient(135deg,#2e4a63,#c98a4a 40%,#3d6a86)"></div>
    <div class="icon"><svg viewBox="0 0 34 34"><rect x="4" y="10" width="12" height="18"/><rect x="18" y="6" width="10" height="22"/><path d="M7 15h6M7 20h6M21 11h4M21 16h4"/></svg></div>
    <h3>Precious Metals Refining</h3>
    <p>Lorem ipsum dolor sit amet, consectetur adipiscing elit, sed do eiusmod</p>
    <a class="more" href="#">READ MORE <svg viewBox="0 0 16 16"><circle cx="8" cy="8" r="8" fill="#0054AA"/><path d="M6.5 4.5L10 8l-3.5 3.5" stroke="#fff" stroke-width="2" fill="none"/></svg></a>
  </article>

  <article class="card" style="left:457px;top:125px">
    <div class="photo" role="img" aria-label="Offshore drilling rig at sea" style="background:linear-gradient(180deg,#5d90c0,#a9c6de 50%,#6b5a44 70%,#2d5878)"></div>
    <div class="icon"><svg viewBox="0 0 34 34"><rect x="5" y="16" width="18" height="12"/><path d="M23 20h6v8h-6M9 16V8h6v8M26 6v14"/></svg></div>
    <h3>Offshore Drilling</h3>
    <p>Lorem ipsum dolor sit amet, consectetur adipiscing elit, sed do eiusmod</p>
    <a class="more" href="#">READ MORE <svg viewBox="0 0 16 16"><circle cx="8" cy="8" r="8" fill="#0054AA"/><path d="M6.5 4.5L10 8l-3.5 3.5" stroke="#fff" stroke-width="2" fill="none"/></svg></a>
  </article>

  <article class="card" style="left:769px;top:125px">
    <div class="photo" role="img" aria-label="Technician in red working at a control panel" style="background:linear-gradient(135deg,#1f2a36,#8a2a24 45%,#2a3440)"></div>
    <div class="icon"><svg viewBox="0 0 34 34"><rect x="5" y="18" width="24" height="8"/><rect x="10" y="8" width="14" height="10"/><circle cx="10" cy="29" r="2"/><circle cx="17" cy="29" r="2"/><circle cx="24" cy="29" r="2"/></svg></div>
    <h3>Production Platform</h3>
    <p>Lorem ipsum dolor sit amet, consectetur adipiscing elit, sed do eiusmod</p>
    <a class="more" href="#">READ MORE <svg viewBox="0 0 16 16"><circle cx="8" cy="8" r="8" fill="#0054AA"/><path d="M6.5 4.5L10 8l-3.5 3.5" stroke="#fff" stroke-width="2" fill="none"/></svg></a>
  </article>

  <article class="card" style="left:144px;top:518px">
    <div class="photo" role="img" aria-label="Large mining excavator under a cloudy sky" style="background:linear-gradient(180deg,#6d8eb0,#b7c6d4 55%,#4a4a48)"></div>
    <div class="icon"><svg viewBox="0 0 34 34"><path d="M4 28h26M7 28V18h8v10M19 28V12h8v16M11 18V8l4-3"/></svg></div>
    <h3>Open Cut &amp; Underground Mining</h3>
    <p>Lorem ipsum dolor sit amet, consectetur adipiscing elit, sed do eiusmod</p>
    <a class="more" href="#">READ MORE <svg viewBox="0 0 16 16"><circle cx="8" cy="8" r="8" fill="#0054AA"/><path d="M6.5 4.5L10 8l-3.5 3.5" stroke="#fff" stroke-width="2" fill="none"/></svg></a>
  </article>

  <article class="card" style="left:457px;top:518px">
    <div class="photo" role="img" aria-label="Workers in hi-vis vests on a wet construction site" style="background:linear-gradient(180deg,#4a3a30,#b86a2a 50%,#3e3630)"></div>
    <div class="icon"><svg viewBox="0 0 34 34"><rect x="7" y="8" width="20" height="20"/><path d="M12 13h3M19 13h3M12 18h3M19 18h3M15 28v-5h4v5"/></svg></div>
    <h3>Civils</h3>
    <p>Lorem ipsum dolor sit amet, consectetur adipiscing elit, sed do eiusmod</p>
    <a class="more" href="#">READ MORE <svg viewBox="0 0 16 16"><circle cx="8" cy="8" r="8" fill="#0054AA"/><path d="M6.5 4.5L10 8l-3.5 3.5" stroke="#fff" stroke-width="2" fill="none"/></svg></a>
  </article>

  <article class="card" style="left:769px;top:518px">
    <div class="photo" role="img" aria-label="Worker overlooking an open-pit quarry" style="background:linear-gradient(180deg,#9bb3c8,#c9a078 50%,#6e5a48)"></div>
    <div class="icon"><svg viewBox="0 0 34 34"><path d="M17 5v10M10 15h14l-3 8h-8zM6 28c4-4 18-4 22 0"/></svg></div>
    <h3>Geotechnical &amp; Construction</h3>
    <p>Lorem ipsum dolor sit amet, consectetur adipiscing elit, sed do eiusmod</p>
    <a class="more" href="#">READ MORE <svg viewBox="0 0 16 16"><circle cx="8" cy="8" r="8" fill="#0054AA"/><path d="M6.5 4.5L10 8l-3.5 3.5" stroke="#fff" stroke-width="2" fill="none"/></svg></a>
  </article>

  <a class="btn" href="#" style="left:463px;top:933px;width:276px;height:43px;font-size:13.5px">Contact Us for a Free Quote <svg viewBox="0 0 16 16"><circle cx="8" cy="8" r="8" fill="#fff"/><path d="M6.5 4.5L10 8l-3.5 3.5" stroke="#0054AA" stroke-width="2" fill="none"/></svg></a>
</section>

<section class="abs testi">
  <h2>CLIENTS TESTIMONIAL</h2>
  <div class="arrow" style="left:58px"><svg viewBox="0 0 22 34"><path d="M18 3L4 17l14 14"/></svg></div>
  <div class="arrow" style="left:1120px"><svg viewBox="0 0 22 34"><path d="M4 3l14 14L4 31"/></svg></div>

  <div class="quote" style="left:196px">
    <div class="q">&ldquo;</div>
    <p>Sed ut perspiciatis unde omnis iste natus sit voluptatem accusantium doloremque laudantium, totam rem aperiam,</p>
    <div class="name">John Doe</div>
    <div class="stars">★★★★★</div>
  </div>
  <div class="avatar" style="left:148px" role="img" aria-label="Client portrait"></div>

  <div class="quote" style="left:673px">
    <div class="q">&ldquo;</div>
    <p>Sed ut perspiciatis unde omnis iste natus sit voluptatem accusantium doloremque laudantium, totam rem aperiam,</p>
    <div class="name">John Doe</div>
    <div class="stars">★★★★★</div>
  </div>
  <div class="avatar" style="left:624px" role="img" aria-label="Client portrait"></div>
</section>

<section class="work">
  <h2 class="h-section" style="top:2818px">OUR WORK</h2>
  <div class="work-tile" style="left:152px;top:2887px;width:443px;height:261px;background:linear-gradient(180deg,#6a7f9a,#e0a257 45%,#8a5a34 60%,#3b4a5e)" role="img" aria-label="Offshore platform at sunset"></div>
  <div class="work-tile" style="left:605px;top:2887px;width:443px;height:261px;background:linear-gradient(180deg,#6f9fcf,#a8c6e2 60%,#4d5a66)" role="img" aria-label="Port cranes on a harbour wharf"></div>
  <div class="work-tile" style="left:152px;top:3157px;width:292px;height:261px;background:linear-gradient(180deg,#7a9ec0,#d8a060 55%,#6a5a4a)" role="img" aria-label="Tower cranes over a high-rise build"></div>
  <div class="work-tile" style="left:454px;top:3157px;width:292px;height:261px;background:linear-gradient(180deg,#7f8fb2,#6a7aa0)" role="img" aria-label="Processing plant interior">
    <div class="zoom"><svg viewBox="0 0 20 20"><circle cx="8" cy="8" r="6"/><path d="M12.5 12.5L18 18M8 5v6M5 8h6"/></svg></div>
  </div>
  <div class="work-tile" style="left:755px;top:3157px;width:293px;height:261px;background:linear-gradient(135deg,#d88a3a,#a8602a 50%,#4a3a30)" role="img" aria-label="Excavator working on earthworks"></div>
  <a class="btn" href="#" style="left:513px;top:3465px;width:174px;height:43px;font-size:13.5px">View All Work <svg viewBox="0 0 16 16"><circle cx="8" cy="8" r="8" fill="#fff"/><path d="M6.5 4.5L10 8l-3.5 3.5" stroke="#0054AA" stroke-width="2" fill="none"/></svg></a>
</section>

<footer class="abs footer">
  <div class="f-logo"><span class="mark"></span>OSTREVANE</div>
  <div class="f-social"><span></span><span></span><span></span><span></span></div>

  <div class="f-col" style="left:418px">
    <h4>Quick Links</h4>
    <ul><li>Home</li><li>Our Services</li><li>About Us</li><li>Our Work</li><li>Contact Us</li></ul>
  </div>
  <div class="f-col" style="left:617px">
    <h4>About Company</h4>
    <ul><li>Legal Information</li><li>Terms &amp; Condition</li><li>Privacy Policy</li><li>Support</li><li>Site Map</li><li>FAQ</li></ul>
  </div>
  <div class="f-col" style="left:836px;width:220px">
    <h4>Contact Us</h4>
    <div class="contact-row"><svg viewBox="0 0 24 24"><path d="M6.6 10.8a15 15 0 006.6 6.6l2.2-2.2c.3-.3.7-.4 1-.2 1.1.4 2.3.6 3.6.6.6 0 1 .4 1 1V20c0 .6-.4 1-1 1A17 17 0 013 4c0-.6.4-1 1-1h3.5c.6 0 1 .4 1 1 0 1.3.2 2.5.6 3.6.1.3 0 .7-.2 1z"/></svg><div><b>Phone</b><span>+1 555 010 2040</span></div></div>
    <div class="contact-row"><svg viewBox="0 0 24 24"><path d="M2 5h20v14H2z M2 5l10 7 10-7" /></svg><div><b>Email</b><span>info@ostrevanemaint.com</span></div></div>
    <div class="contact-row"><svg viewBox="0 0 24 24"><path d="M12 2a7 7 0 00-7 7c0 5 7 13 7 13s7-8 7-13a7 7 0 00-7-7zm0 9.5A2.5 2.5 0 1112 6a2.5 2.5 0 010 5.5z"/></svg><div><b>Location</b><span>22 Harbour Lane, Fremantle, WA 6160</span></div></div>
  </div>

  <div class="f-line"></div>
  <div class="to-top"><svg viewBox="0 0 14 14"><path d="M2 9l5-5 5 5"/></svg></div>
  <div class="copy">2024 Copyright - Ostrevane Maintenance | All Rights Reserved</div>
</footer>

</body>
</html>
```